Harborne Cellarbook: the premier wine registry - (need business cards)

We have a logo designed, and now we need business cards for our 3 founders. Harborne Cellarbook is the premier wine registry for weddings. I am envisioning the wine glass with the heart in it as our signature symbol. (FYI- on the red background file, only use the part that has the red background; the brown colors are not relevant)

```html
<!DOCTYPE html>
<html lang="en">
<head>
<meta charset="utf-8">
<title>Harborne Cellarbook — Business Cards</title>
<link href="https://fonts.googleapis.com/css2?family=Questrial&display=swap" rel="stylesheet">
<style>
  :root {
    --backdrop: #2a2b2f;
    --card: #1d1f22;
    --card-edge: #26282c;
    --spot-gloss: #34373b;
    --ink-light: #e4e4e6;
    --ink-soft: #c9c9cc;
    --wine: #9c1f4f;
  }
  * { margin: 0; padding: 0; box-sizing: border-box; }
  html, body {
    width: 1200px;
    height: 800px;
    overflow: hidden;
    background: var(--backdrop);
    font-family: "Questrial", "Helvetica Neue", Arial, sans-serif;
  }
  .stage {
    position: relative;
    width: 1200px;
    height: 800px;
  }
  .card {
    position: absolute;
    left: 348px;
    width: 504px;
    height: 288px;
    background: var(--card);
    border: 1px solid var(--card-edge);
    border-radius: 18px;
    box-shadow: 0 14px 30px rgba(0, 0, 0, 0.45);
    overflow: hidden;
  }
  .card--back { top: 92px; }
  .card--front { top: 420px; }

  .wordmark {
    display: flex;
    align-items: center;
    gap: 12px;
    text-transform: uppercase;
    white-space: nowrap;
  }
  .wordmark__dot {
    border-radius: 50%;
    flex: none;
  }
  .wordmark__name {
    display: flex;
    flex-direction: column;
    letter-spacing: 0.1em;
    line-height: 1.15;
  }

  .card--back .wordmark {
    position: absolute;
    left: 50%;
    top: 50%;
    transform: translate(-50%, -50%);
    color: var(--spot-gloss);
    font-size: 30px;
    gap: 14px;
  }
  .card--back .wordmark__dot {
    width: 26px;
    height: 26px;
    background: var(--spot-gloss);
  }

  .card--front .wordmark {
    position: absolute;
    left: 36px;
    top: 118px;
    font-size: 22px;
    gap: 10px;
    color: var(--ink-light);
  }
  .card--front .wordmark__dot {
    width: 20px;
    height: 20px;
    background: var(--wine);
  }

  .divider {
    position: absolute;
    left: 262px;
    top: 74px;
    width: 1px;
    height: 140px;
    background: var(--wine);
  }

  .contact {
    position: absolute;
    left: 282px;
    top: 78px;
    color: var(--ink-soft);
    font-size: 11px;
    line-height: 1.55;
  }
  .contact__name {
    font-size: 15px;
    letter-spacing: 0.03em;
    color: var(--ink-light);
  }
  .contact__name .first { color: var(--wine); }
  .contact__role { margin-bottom: 6px; }
  .contact__row {
    display: flex;
    align-items: center;
    gap: 7px;
    margin-top: 3px;
  }
  .contact__icon {
    width: 14px;
    height: 14px;
    flex: none;
  }
</style>
</head>
<body>
  <main class="stage">
    <section class="card card--back" aria-label="Card back">
      <div class="wordmark">
        <span class="wordmark__dot"></span>
        <span class="wordmark__name"><span>Harborne</span><span>Cellarbook</span></span>
      </div>
    </section>

    <section class="card card--front" aria-label="Card front">
      <div class="wordmark">
        <span class="wordmark__dot"></span>
        <span class="wordmark__name"><span>Harborne</span><span>Cellarbook</span></span>
      </div>

      <div class="divider"></div>

      <div class="contact">
        <p class="contact__name"><span class="first">MARLA</span> QUINN</p>
        <p class="contact__role">Founder</p>
        <p>4120 W. Orchard Ln.</p>
        <p>Suite 2, Calder Falls 60418</p>
        <p class="contact__row">
          <svg class="contact__icon" viewBox="0 0 14 14" aria-hidden="true">
            <circle cx="7" cy="7" r="7" fill="var(--wine)"/>
            <path d="M4.3 3.6c.4-.3.9-.2 1.1.2l.6 1.2c.2.3.1.7-.2.9l-.5.4c.4.9 1.1 1.6 2 2l.4-.5c.2-.3.6-.4.9-.2l1.2.6c.4.2.5.7.2 1.1l-.5.6c-.4.4-1 .5-1.5.3C6.1 9.5 4.5 7.9 3.8 6c-.2-.5-.1-1.1.3-1.5z" fill="var(--ink-light)"/>
          </svg>
          <span>555-014-2290</span>
        </p>
        <p class="contact__row">
          <svg class="contact__icon" viewBox="0 0 14 14" aria-hidden="true">
            <circle cx="7" cy="7" r="7" fill="var(--wine)"/>
            <rect x="3.5" y="4.6" width="7" height="4.8" rx="0.6" fill="var(--ink-light)"/>
            <path d="M3.7 4.9L7 7.4l3.3-2.5" fill="none" stroke="var(--wine)" stroke-width="0.8"/>
          </svg>
          <span>hello@cellarbook.com</span>
        </p>
      </div>
    </section>
  </main>
</body>
</html>
```